Business card design for Automotive workshop

We need a business card for a new automotive repair and tyre shop called Ridgeback Prime Automotive located in New Zealand. We are a clean, modern and fresh workshop and company.

Front needs to feature logo,
my name:
Lachie Westergaard (director)

Address:
48 Marlow Lane
Whitianga 3510

Phone: 07 842 1937
Mobile: 027 519 2764
Email: office@ridgebackmotors.co.nz
Website: ridgebackmotors.co.nz

Back needs to feature an area to write down appointment details, date and time.

Also feature a list of jobs and work we do such as,
Vehicle Servicing
All Mechanical Repairs
Warrant of Fitness
Tyres & Wheel Alignments
Automotive Diagnostics
Automotive Parts & Supplies

```html
<!DOCTYPE html>
<html lang="en">
<head>
<meta charset="utf-8">
<title>Ridgeback Prime Automotive – Business Card</title>
<link rel="stylesheet" href="https://fonts.googleapis.com/css2?family=Arimo:ital,wght@0,400;0,700;1,400&display=swap">
<style>
  :root {
    --stage: #3a3a3a;
    --card-light: #a9bfd2;
    --card-mid: #93adc4;
    --card-dark: #8aa4bb;
    --accent-red: #e1232b;
    --ink: #111111;
    --paper-white: #ffffff;
  }
  * { box-sizing: border-box; margin: 0; padding: 0; }
  html, body {
    width: 1200px; height: 1195px; overflow: hidden;
    background: var(--stage);
    font-family: "Arimo", Arial, sans-serif;
  }
  .card {
    position: absolute; left: 160px;
    width: 880px; height: 503px;
    overflow: hidden;
    background: linear-gradient(135deg, var(--card-mid) 0%, var(--card-light) 45%, var(--card-dark) 100%);
    box-shadow: 0 14px 30px rgba(0,0,0,0.45);
  }
  .card--back { top: 50px; }
  .card--front { top: 632px; }

  /* Back */
  .brand-name {
    font-weight: 700; text-transform: uppercase;
    letter-spacing: 1px; white-space: nowrap;
  }
  .card--back .brand-name {
    position: absolute; left: 0; right: 0; top: 95px; text-align: center;
    color: var(--accent-red); font-size: 34px;
  }
  .service-list { position: absolute; list-style: none; color: var(--paper-white); font-size: 22px; letter-spacing: 0.6px; }
  .service-list li { position: relative; padding-left: 20px; margin-bottom: 9px; }
  .service-list li::before,
  .write-line .label::before {
    content: ""; position: absolute; left: 0; top: 8px;
    width: 10px; height: 10px; border-radius: 50%; background: var(--accent-red);
  }
  .service-list--left { left: 95px; top: 245px; }
  .service-list--right { left: 500px; top: 175px; }
  .divider { position: absolute; left: 450px; top: 175px; width: 4px; height: 120px; background: var(--paper-white); }
  .write-line { position: absolute; display: flex; align-items: flex-end; color: var(--paper-white); font-size: 22px; }
  .write-line .label { position: relative; padding-left: 20px; margin-right: 10px; }
  .write-line .rule { height: 4px; background: var(--paper-white); margin-bottom: 4px; }
  .write-line--time { left: 500px; top: 325px; }
  .write-line--time .rule { width: 260px; }
  .write-line--date { left: 95px; top: 425px; }
  .write-line--date .rule { width: 330px; }

  /* Front */
  .holder { position: absolute; left: 120px; top: 70px; color: var(--ink); }
  .holder__name { display: flex; align-items: center; gap: 10px; font-size: 33px; font-weight: 700; letter-spacing: 1.5px; }
  .holder__role { font-size: 27px; margin: 2px 0 0 40px; letter-spacing: 1px; }
  .holder__rule { position: absolute; left: 115px; top: 165px; width: 360px; height: 7px; border-radius: 4px; background: var(--ink); }
  .contact-list { position: absolute; left: 90px; top: 205px; list-style: none; color: var(--ink); font-size: 22px; font-style: italic; letter-spacing: 0.8px; }
  .contact-list li { display: flex; align-items: center; gap: 10px; height: 38px; }
  .contact-list li:last-child { font-style: normal; }
  .icon { width: 24px; height: 24px; flex: none; }
  .brand-pill {
    position: absolute; left: 470px; top: 230px; width: 390px; height: 92px;
    border-radius: 46px; background: var(--ink);
    display: flex; align-items: center; justify-content: center;
    padding: 0 24px;
  }
  .card--front .brand-name { color: var(--paper-white); font-size: 18px; letter-spacing: 0.5px; }
</style>
</head>
<body>

<section class="card card--back" aria-label="Card back">
  <p class="brand-name">Ridgeback Prime Automotive</p>
  <ul class="service-list service-list--left">
    <li>Vehicle Servicing</li>
    <li>All Mechanical Repairs</li>
    <li>Warrant of Fitness</li>
  </ul>
  <div class="divider"></div>
  <ul class="service-list service-list--right">
    <li>Tyres &amp; Wheel Alignments</li>
    <li>Automotive Parts &amp; Supplies</li>
    <li>Automotive Diagnostics</li>
  </ul>
  <div class="write-line write-line--time"><span class="label">Time</span><span class="rule"></span></div>
  <div class="write-line write-line--date"><span class="label">Date</span><span class="rule"></span></div>
</section>

<section class="card card--front" aria-label="Card front">
  <div class="holder">
    <p class="holder__name">
      <svg class="icon" viewBox="0 0 24 24" aria-hidden="true"><circle cx="12" cy="12" r="11" fill="#111"/><circle cx="12" cy="6.5" r="2" fill="#a9bfd2"/><rect x="10.3" y="10" width="3.4" height="9" rx="1" fill="#a9bfd2"/></svg>
      Lachie Westergaard
    </p>
    <p class="holder__role">(Managing director)</p>
  </div>
  <div class="holder__rule"></div>

  <ul class="contact-list">
    <li>
      <svg class="icon" viewBox="0 0 24 24" aria-hidden="true"><circle cx="12" cy="12" r="11" fill="#111"/><path d="M8 6c1 0 2 2 2 3s-1 1-1 2 2 4 4 4 1-1 2-1 3 1 3 2-1 2-3 2C10 18 6 12 6 8c0-1 1-2 2-2z" fill="#a9bfd2"/></svg>
      027 519 2764
    </li>
    <li>
      <svg class="icon" viewBox="0 0 24 24" aria-hidden="true"><circle cx="12" cy="12" r="11" fill="#111"/><path d="M5 10c0-3 14-3 14 0v1h-3v-1H8v1H5z" fill="#a9bfd2"/><rect x="7" y="12" width="10" height="6" rx="1" fill="#a9bfd2"/><circle cx="12" cy="15" r="1.6" fill="#111"/></svg>
      07 842 1937
    </li>
    <li>
      <svg class="icon" viewBox="0 0 24 24" aria-hidden="true"><circle cx="12" cy="12" r="11" fill="#111"/><rect x="6" y="8" width="12" height="8" fill="#a9bfd2"/><path d="M6 8l6 5 6-5" fill="none" stroke="#111" stroke-width="1.4"/></svg>
      office@ridgebackmotors.co.nz
    </li>
    <li>
      <svg class="icon" viewBox="0 0 24 24" aria-hidden="true"><circle cx="12" cy="12" r="11" fill="#111"/><circle cx="12" cy="12" r="6.5" fill="none" stroke="#a9bfd2" stroke-width="1.5"/><ellipse cx="12" cy="12" rx="2.8" ry="6.5" fill="none" stroke="#a9bfd2" stroke-width="1.3"/><path d="M5.5 12h13" stroke="#a9bfd2" stroke-width="1.3"/></svg>
      ridgebackmotors.co.nz
    </li>
    <li>
      <svg class="icon" viewBox="0 0 24 24" aria-hidden="true"><circle cx="12" cy="12" r="11" fill="#111"/><path d="M5.5 12.5L12 6.5l6.5 6H17v5h-3.5v-3.5h-3V17.5H7v-5z" fill="#a9bfd2"/></svg>
      48 Marlow Lane Whitianga 3510
    </li>
  </ul>

  <div class="brand-pill">
    <p class="brand-name">Ridgeback Prime Automotive</p>
  </div>
</section>

</body>
</html>
```